Marrowind Labs - pioneers of next generation consulting!

We are a next generation management consulting firm with two focus areas and USPs (unique selling points):>Technology driven business developmentWe are not developers, we are experts in HOW to apply and incorporate technology in your business dna to drive business growth and value-added change.>Creating high performing teams levering our philosophy of collective intelligence. We truly understand the need of human engagement and we know that the only way of getting there is by building strong relationships among people, a warm and open culture is a stepping stone towards effective collaboration within/among teams. - We don't want a ”corporate feel” to our templates. The organic feeling we have with our blue-on-blue blobs has the idea of ever changing movement and shape changing. Please see our website, www.marrowindlabs.se. - In our context we sit among classic business mgmt. consultants and classic IT mgmt. consultants. We cater to business, tech and humans as the ultimate vehicle of change and business value. -To have a clean template one suggestion is to only use blue, white and black and keeping other colors separate, as an alternative but we are truly open allow your creativity add value to this. We are looking to find a slide deck which we can pick slides from, depending on what/whom/why we interact with customer we want to create different outcomes and our presentations should support this.

Industry/Entity Type

Management Consulting

Requirements
Must have
• next generation powerpoint and how to package storytelling. please keep to our look and feel, we just arrived at our logo, colours and shapes. Help us to carry it into our ppt's as well.
Should not have
• Hi all, please have a look at our website. It is still very new and more will be done, but our goal is to make powerpoint to come alive again and mirror our pioneering hearts and brains.

```html
<!DOCTYPE html>
<html lang="en">
<head>
<meta charset="utf-8">
<title>Marrowind Labs – Slide Deck</title>
<link rel="stylesheet" href="https://fonts.googleapis.com/css2?family=Nunito+Sans:ital,wght@0,400;0,700;0,800;1,400&display=swap">
<style>
:root{
  --blue:#2d5fb2;
  --navy:#1d3c85;
  --sky:#4a86d8;
  --green:#3eae5c;
  --ink:#26324d;
  --grey:#6b7385;
  --page:#e6e7e9;
  --white:#ffffff;
}
*{margin:0;padding:0;box-sizing:border-box}
html,body{width:1200px;height:2500px;overflow:hidden;background:var(--page)}
body{position:relative;font-family:'Nunito Sans',sans-serif;color:var(--ink)}
.slide{position:absolute;width:367px;height:207px;overflow:hidden;background:var(--white)}
.slide.is-blue{background:var(--blue);color:var(--white)}
.hero-left{left:75px;top:162px;transform:scale(1.316);transform-origin:0 0;box-shadow:0 4px 14px rgba(0,0,0,.12)}
.hero-right{left:600px;top:60px;transform:scale(1.417);transform-origin:0 0;box-shadow:0 4px 14px rgba(0,0,0,.12)}
.layer{position:absolute;inset:0;width:100%;height:100%}
.abs{position:absolute}
.title{font-size:11px;font-weight:800;text-transform:uppercase;color:var(--navy);letter-spacing:.2px}
.is-blue .title{color:var(--white)}
.sub{font-size:6px;font-weight:700;color:var(--navy)}
.is-blue .sub{color:var(--white)}
.body{font-size:5px;line-height:1.45;color:var(--grey)}
.is-blue .body{color:#dfe8f7}
.bul p{font-size:5px;line-height:1.4;color:var(--grey);margin-bottom:1.5px}
.bul p.in{padding-left:7px}
.is-blue .bul p{color:#e4ecf8}
.foot{position:absolute;left:12px;right:12px;bottom:7px;display:flex;justify-content:space-between;align-items:center}
.brand{font-size:7px;font-weight:800;text-transform:uppercase;letter-spacing:.4px;color:var(--navy)}
.is-blue .brand,.brand.on-dark{color:var(--white)}
.url{font-size:4.5px;color:var(--grey);display:flex;align-items:center;gap:4px}
.is-blue .url{color:#dfe8f7}
.url i{display:inline-block;width:7px;height:7px;border-radius:50%;background:var(--navy)}
.is-blue .url i{background:var(--white)}
.big-brand{font-size:13px;font-weight:800;text-transform:uppercase;letter-spacing:.6px}
.pres{font-size:12px;font-weight:800;text-transform:uppercase;line-height:1}
.photo{background:linear-gradient(135deg,#9aa3b3,#5d6a80)}
.quote{font-size:6px;font-style:italic;line-height:1.45}
.toc li{list-style:none;display:flex;gap:6px;align-items:flex-start;margin-bottom:4px}
.toc b{flex:none;width:10px;height:10px;border-radius:50%;background:var(--navy);color:#fff;font-size:6px;display:flex;align-items:center;justify-content:center}
.toc b.g{background:var(--green)}
.toc strong{display:block;font-size:5.5px;color:var(--navy);text-transform:uppercase}
.toc strong.g{color:var(--green)}
.toc span{font-size:4.5px;color:var(--grey)}
.cell{position:absolute;width:36px;height:30px}
.cell.txt{background:var(--blue);color:#fff;padding:3px;font-size:3.6px;line-height:1.35}
.cell.txt.g{background:var(--green)}
.cell.txt strong{display:block;font-size:4.2px}
.ic-row{position:absolute;display:flex;gap:5px;align-items:center}
.ic-row strong{display:block;font-size:5px;color:var(--navy);text-transform:uppercase}
.ic-row span{display:block;font-size:4.3px;color:var(--grey);line-height:1.35}
.centered{text-align:center}
.person strong{display:block;font-size:5.5px;color:var(--navy);margin-top:3px}
.person span{display:block;font-size:4.3px;color:var(--grey);line-height:1.35}
.tile{position:absolute;color:#fff;padding:6px 8px}
.tile strong{display:block;font-size:6px;text-transform:uppercase}
.tile span{font-size:4.3px;line-height:1.35;display:block}
</style>
</head>
<body>

<svg width="0" height="0" style="position:absolute" aria-hidden="true">
  <defs>
    <linearGradient id="ph" x1="0" y1="0" x2="1" y2="1">
      <stop offset="0" stop-color="#a7afbd"/><stop offset="1" stop-color="#5b677c"/>
    </linearGradient>
    <linearGradient id="phw" x1="0" y1="0" x2="1" y2="1">
      <stop offset="0" stop-color="#c6cad2"/><stop offset="1" stop-color="#8d96a6"/>
    </linearGradient>
  </defs>
</svg>

<!-- Hero: profile slide -->
<section class="slide is-blue hero-left">
  <svg class="layer" viewBox="0 0 367 207" preserveAspectRatio="none">
    <path d="M0 0H190C222 40 212 120 178 160C150 195 90 205 0 190Z" fill="#fff"/>
    <path role="img" aria-label="Portrait of a consultant in a blazer" d="M245 30C270 10 320 15 335 50C352 90 340 140 305 160C270 180 225 165 210 130C195 95 215 55 245 30Z" fill="url(#ph)"/>
  </svg>
  <div class="abs" style="left:20px;top:22px;width:150px">
    <div class="title">John Doe</div>
    <div class="sub" style="font-weight:400;color:var(--ink);margin-top:2px">Lorem ipsum dolor sit amet,<br>consectetur adipiscing elit</div>
    <p class="quote" style="color:var(--blue);margin-top:10px">“ Lorem Ipsum is simply dummy text of the printing and industry. Lorem Ipsum has been the industry's standard dummy text ever since the 1500s, when an unknown printer took a galley of type and scrembled it to make a type specimen book ”</p>
    <p class="body" style="margin-top:3px">- John Doe</p>
  </div>
  <div class="foot"><span class="brand">Marrowind Labs</span><span class="url">www.marrowindlabs.se <i></i></span></div>
</section>

<!-- Hero: title slide -->
<section class="slide is-blue hero-right">
  <svg class="layer" viewBox="0 0 367 207" preserveAspectRatio="none">
    <path d="M0 0H200C225 50 215 140 180 180C165 198 150 207 140 207H0Z" fill="var(--navy)"/>
    <path role="img" aria-label="Photo of a white humanoid robot" d="M0 0H178C200 50 192 135 160 172C145 192 125 207 110 207H0Z" fill="url(#phw)"/>
  </svg>
  <div class="abs" style="left:212px;top:60px">
    <div class="big-brand">Marrowind Labs</div>
    <div style="height:1px;width:90px;background:#fff;margin:10px 0 8px"></div>
    <div class="pres">Presentation Title</div>
    <div style="font-size:6px;margin-top:2px">Sub Presentation Title</div>
    <div style="font-size:5.5px;margin-top:10px">April, 2018</div>
  </div>
</section>

<!-- Row 1 -->
<section class="slide is-blue" style="left:33px;top:687px">
  <svg class="layer" viewBox="0 0 367 207" preserveAspectRatio="none">
    <path d="M0 0H170C195 50 185 140 150 180C135 198 120 207 110 207H0Z" fill="var(--navy)"/>
    <path role="img" aria-label="Photo of a white humanoid robot" d="M0 0H150C172 50 165 135 135 172C120 192 100 207 85 207H0Z" fill="url(#phw)"/>
  </svg>
  <div class="abs" style="left:195px;top:55px">
    <div class="big-brand">Marrowind Labs</div>
    <div style="height:1px;width:80px;background:#fff;margin:8px 0 7px"></div>
    <div class="pres">Presentation Title</div>
    <div style="font-size:6px;margin-top:2px">Sub Presentation Title</div>
    <div style="font-size:5.5px;margin-top:9px">April, 2018</div>
  </div>
</section>

<section class="slide" style="left:417px;top:687px">
  <svg class="layer" viewBox="0 0 367 207" preserveAspectRatio="none">
    <path d="M0 0H170C195 50 185 140 150 180C135 198 120 207 110 207H0Z" fill="var(--blue)"/>
    <path role="img" aria-label="Photo of a white humanoid robot" d="M0 0H150C172 50 165 135 135 172C120 192 100 207 85 207H0Z" fill="url(#phw)"/>
  </svg>
  <div class="abs" style="left:195px;top:55px;color:var(--navy)">
    <div class="big-brand">Marrowind Labs</div>
    <div style="height:1px;width:80px;background:var(--navy);margin:8px 0 7px"></div>
    <div class="pres">Presentation Title</div>
    <div style="font-size:6px;margin-top:2px">Sub Presentation Title</div>
    <div style="font-size:5.5px;margin-top:9px">April, 2018</div>
  </div>
</section>

<section class="slide is-blue" style="left:800px;top:687px">
  <svg class="layer" viewBox="0 0 367 207" preserveAspectRatio="none">
    <path d="M367 0V150C320 140 270 150 215 130C160 110 100 50 110 0Z" fill="var(--navy)"/>
    <path role="img" aria-label="Photo of people in a lively group discussion" d="M367 0V135C320 125 270 135 225 118C170 98 120 45 130 0Z" fill="url(#ph)"/>
  </svg>
  <div class="abs" style="left:12px;top:135px">
    <div style="font-size:11px;font-weight:800">Section Slide</div>
    <div style="font-size:5.5px;margin-top:2px">Sub Divider Presentation</div>
  </div>
  <div class="brand abs" style="right:12px;bottom:8px">Marrowind Labs</div>
</section>

<!-- Row 2 -->
<section class="slide" style="left:33px;top:912px">
  <svg class="layer" viewBox="0 0 367 207" preserveAspectRatio="none">
    <path d="M0 0H110C145 40 150 110 120 150C95 185 45 190 0 175Z" fill="var(--blue)"/>
  </svg>
  <div class="abs" style="left:22px;top:72px;color:#fff;font-size:11px;font-weight:800;line-height:1.1">TABLE OF<br>CONTENT</div>
  <ul class="toc abs" style="left:190px;top:18px">
    <li><b>1</b><div><strong>About us</strong><span>Lorem ipsum dolor sit amet</span></div></li>
    <li><b>2</b><div><strong>How we do</strong><span>Lorem ipsum dolor sit amet</span></div></li>
    <li><b class="g">3</b><div><strong class="g">Business process</strong><span>Lorem ipsum dolor sit amet</span></div></li>
    <li><b>4</b><div><strong>Our team</strong><span>Lorem ipsum dolor sit amet</span></div></li>
    <li><b>5</b><div><strong>Our activity</strong><span>Lorem ipsum dolor sit amet</span></div></li>
    <li><b class="g">6</b><div><strong class="g">Contact us</strong><span>Lorem ipsum dolor sit amet</span></div></li>
  </ul>
  <div class="foot"><span class="brand">Marrowind Labs</span><span class="url">www.marrowindlabs.se <i></i></span></div>
</section>

<section class="slide" style="left:417px;top:912px">
  <div class="abs" style="left:14px;top:12px;right:14px">
    <div class="title">One Column</div>
    <div style="height:1px;background:#c9d3e6;margin:5px 0"></div>
    <div class="sub">Lorem Ipsum</div>
    <div class="bul" style="margin-top:3px">
      <p>•Lorem ipsum dolor sit amet, te ulum corpora delicata duo. Rebum insolens pri eu. No alia tota modus qui.</p>
      <p class="in">•Vel brute ei usu. Duo isque appareat adversarium ei</p>
      <p>•Lorem ipsum dolor sit amet, te ulum corpora delicata duo. Rebum insolens pri eu. No alia tota modus qui.</p>
      <p class="in">•Vel brute ei usu. Duo isque appareat adversarium ei</p>
      <p>•Lorem ipsum dolor sit amet, te ulum corpora delicata duo. Rebum insolens pri eu. No alia tota modus qui.</p>
      <p class="in">•Vel brute ei usu. Duo isque appareat adversarium ei</p>
    </div>
  </div>
  <div class="foot"><span class="brand">Marrowind Labs</span><span class="url">www.marrowindlabs.se <i></i></span></div>
</section>

<section class="slide is-blue" style="left:800px;top:912px">
  <div class="abs" style="left:14px;top:12px;right:14px">
    <div class="title">One Column</div>
    <div style="height:1px;background:#7da0da;margin:5px 0"></div>
    <div class="sub">Lorem Ipsum</div>
    <div class="bul" style="margin-top:3px">
      <p>•Lorem ipsum dolor sit amet, te ulum corpora delicata duo. Rebum insolens pri eu. No alia tota modus qui.</p>
      <p class="in">•Vel brute ei usu. Duo isque appareat adversarium ei</p>
      <p>•Lorem ipsum dolor sit amet, te ulum corpora delicata duo. Rebum insolens pri eu. No alia tota modus qui.</p>
      <p class="in">•Vel brute ei usu. Duo isque appareat adversarium ei</p>
      <p>•Lorem ipsum dolor sit amet, te ulum corpora delicata duo. Rebum insolens pri eu. No alia tota modus qui.</p>
      <p class="in">•Vel brute ei usu. Duo isque appareat adversarium ei</p>
    </div>
  </div>
  <div class="foot"><span class="brand">Marrowind Labs</span><span class="url">www.marrowindlabs.se <i></i></span></div>
</section>

<!-- Row 3 -->
<section class="slide" style="left:33px;top:1137px">
  <svg class="layer" viewBox="0 0 367 207" preserveAspectRatio="none">
    <path d="M367 0H225C200 40 195 110 210 150C225 190 290 200 367 195Z" fill="var(--blue)"/>
    <g fill="#fff" font-size="5" font-family="Nunito Sans, sans-serif"><text x="265" y="28">Bar Chart Sample</text></g>
    <g stroke="#6f98d8" stroke-width=".5"><line x1="250" y1="45" x2="345" y2="45"/><line x1="250" y1="70" x2="345" y2="70"/><line x1="250" y1="95" x2="345" y2="95"/><line x1="250" y1="120" x2="345" y2="120"/></g>
    <g>
      <rect x="257" y="75" width="6" height="45" fill="var(--navy)"/><rect x="264" y="85" width="6" height="35" fill="#b9cdec"/><rect x="271" y="95" width="6" height="25" fill="var(--green)"/>
      <rect x="288" y="60" width="6" height="60" fill="var(--navy)"/><rect x="295" y="90" width="6" height="30" fill="#b9cdec"/><rect x="302" y="80" width="6" height="40" fill="var(--green)"/>
      <rect x="319" y="70" width="6" height="50" fill="var(--navy)"/><rect x="326" y="78" width="6" height="42" fill="#b9cdec"/><rect x="333" y="55" width="6" height="65" fill="var(--green)"/>
    </g>
    <g fill="#fff" font-size="4" font-family="Nunito Sans, sans-serif"><text x="256" y="128">Category 1</text><text x="287" y="128">Category 2</text><text x="318" y="128">Category 3</text></g>
  </svg>
  <div class="abs" style="left:14px;top:12px;width:185px">
    <div class="title">Left Column</div>
    <div style="height:1px;background:#c9d3e6;margin:5px 0"></div>
    <div class="sub">Lorem Ipsum</div>
    <div class="bul" style="margin-top:3px">
      <p>•Lorem ipsum dolor sit amet, te ulum corpora delicata duo. Rebum insolens pri eu. No alia tota modus qui.</p>
      <p class="in">•Vel brute ei usu. Duo isque appareat adversarium ei</p>
      <p>•Lorem ipsum dolor sit amet, te ulum corpora delicata duo. Rebum insolens pri eu. No alia tota modus qui.</p>
      <p class="in">•Vel brute ei usu. Duo isque appareat adversarium ei</p>
      <p>•Lorem ipsum dolor sit amet, te ulum corpora delicata duo. Rebum insolens pri eu.</p>
    </div>
  </div>
  <div class="foot"><span class="brand">Marrowind Labs</span><span class="url">www.marrowindlabs.se <i></i></span></div>
</section>

<section class="slide" style="left:417px;top:1137px">
  <svg class="layer" viewBox="0 0 367 207" preserveAspectRatio="none">
    <path d="M0 0H150C175 45 170 120 145 160C125 195 60 207 0 207Z" fill="var(--blue)"/>
    <path role="img" aria-label="Photo of hands working on a circuit board" d="M0 0H135C158 45 152 118 128 155C110 185 55 200 0 200Z" fill="url(#ph)"/>
  </svg>
  <div class="abs" style="left:185px;top:12px;right:14px">
    <div class="title">Right Column</div>
    <div style="height:1px;background:#c9d3e6;margin:5px 0"></div>
    <div class="sub">Lorem Ipsum</div>
    <div class="bul" style="margin-top:3px">
      <p>•Lorem ipsum dolor sit amet, te ulum corpora delicata duo. Rebum insolens pri eu. No alia tota modus qui.</p>
      <p class="in">•Vel brute ei usu. Duo isque appareat adversarium ei</p>
      <p>•Lorem ipsum dolor sit amet, te ulum corpora delicata duo. Rebum insolens pri eu. No alia tota modus qui.</p>
      <p class="in">•Vel brute ei usu. Duo isque appareat adversarium ei</p>
      <p>•Lorem ipsum dolor sit amet, te ulum corpora delicata duo. Rebum insolens pri eu.</p>
    </div>
  </div>
  <div class="foot"><span class="brand on-dark">Marrowind Labs</span><span class="url">www.marrowindlabs.se <i></i></span></div>
</section>

<section class="slide" style="left:800px;top:1137px">
  <div class="abs photo" style="inset:0" role="img" aria-label="Photo of a cheerful crowd taking a group selfie"></div>
  <div class="brand on-dark abs" style="left:12px;bottom:8px">Marrowind Labs</div>
</section>

<!-- Row 4 -->
<section class="slide" style="left:33px;top:1362px">
  <div class="abs" style="left:0;top:0;width:367px;height:95px;background:var(--navy)" role="img" aria-label="Blue-toned photo of a team at work"></div>
  <div class="title abs centered" style="left:0;right:0;top:10px;color:#fff">Right Column</div>
  <svg class="layer" viewBox="0 0 367 207" preserveAspectRatio="none">
    <path d="M62 78C80 60 112 62 120 82C128 105 110 122 88 120C64 118 48 95 62 78Z" fill="var(--navy)" stroke="#fff" stroke-width="2"/>
    <path d="M162 76C182 62 212 66 216 88C220 110 198 122 180 118C158 114 146 90 162 76Z" fill="var(--blue)" stroke="#fff" stroke-width="2"/>
    <path d="M260 72C282 62 308 72 306 95C304 115 280 124 264 116C244 106 240 82 260 72Z" fill="var(--green)" stroke="#fff" stroke-width="2"/>
    <g fill="#fff" font-size="4.5" font-weight="700" font-family="Nunito Sans, sans-serif" text-anchor="middle">
      <text x="90" y="103">TEXT HERE</text><text x="183" y="101">TEXT HERE</text><text x="277" y="99">TEXT HERE</text>
    </g>
  </svg>
  <p class="body abs centered" style="left:50px;top:135px;width:80px">Lorem ipsum dolor sit amet, te ulum corpora delicata duo. Rebum insolens pri eu. No alia tota modus qui.</p>
  <p class="body abs centered" style="left:143px;top:135px;width:80px">Lorem ipsum dolor sit amet, te ulum corpora delicata duo. Rebum insolens pri eu. No alia tota modus qui.</p>
  <p class="body abs centered" style="left:237px;top:135px;width:80px">Lorem ipsum dolor sit amet, te ulum corpora delicata duo. Rebum insolens pri eu. No alia tota modus qui.</p>
  <div class="foot"><span class="brand">Marrowind Labs</span><span class="url">www.marrowindlabs.se <i></i></span></div>
</section>

<section class="slide" style="left:417px;top:1362px">
  <div class="title abs" style="left:14px;top:12px">Collaboration Pics</div>
  <div class="abs" style="left:14px;top:28px;width:339px;height:1px;background:#c9d3e6"></div>
  <div class="cell photo" style="left:14px;top:40px;width:50px;height:40px" role="img" aria-label="Photo of a team meeting"></div>
  <div class="cell txt" style="left:68px;top:40px;width:50px;height:40px"><strong>Heading Sample</strong>Lorem ipsum dolor sit amet, delicata duo. Rebum insolens pri eu.</div>
  <div class="cell photo" style="left:122px;top:40px;width:50px;height:40px" role="img" aria-label="Photo of colleagues talking"></div>
  <div class="cell txt g" style="left:176px;top:40px;width:50px;height:40px"><strong>Heading Sample</strong>Lorem ipsum dolor sit amet, delicata duo. Rebum insolens pri eu.</div>
  <div class="cell photo" style="left:230px;top:40px;width:50px;height:40px" role="img" aria-label="Photo of a workshop"></div>
  <div class="cell photo" style="left:284px;top:40px;width:69px;height:40px" role="img" aria-label="Photo of a laptop on a desk"></div>
  <div class="cell txt" style="left:14px;top:84px;width:50px;height:40px"><strong>Heading Sample</strong>Lorem ipsum dolor sit amet, delicata duo. Rebum insolens pri eu.</div>
  <div class="cell photo" style="left:68px;top:84px;width:50px;height:40px" role="img" aria-label="Photo of a presenter"></div>
  <div class="cell txt" style="left:122px;top:84px;width:50px;height:40px"><strong>Heading Sample</strong>Lorem ipsum dolor sit amet, delicata duo. Rebum insolens pri eu.</div>
  <div class="cell photo" style="left:176px;top:84px;width:50px;height:40px" role="img" aria-label="Photo of a group at a table"></div>
  <div class="cell txt" style="left:230px;top:84px;width:50px;height:40px"><strong>Heading Sample</strong>Lorem ipsum dolor sit amet, delicata duo. Rebum insolens pri eu.</div>
  <div class="cell photo" style="left:284px;top:84px;width:69px;height:40px" role="img" aria-label="Photo of people collaborating"></div>
  <div class="foot"><span class="brand">Marrowind Labs</span><span class="url">www.marrowindlabs.se <i></i></span></div>
</section>

<section class="slide is-blue" style="left:800px;top:1362px">
  <svg class="layer" viewBox="0 0 367 207" preserveAspectRatio="none">
    <path d="M0 0H250C270 50 250 130 215 170C195 195 150 207 120 207H0Z" fill="var(--navy)"/>
    <path role="img" aria-label="Photo of two colleagues in conversation" d="M0 0H232C252 50 234 125 200 162C180 188 140 200 110 200H0Z" fill="url(#ph)"/>
  </svg>
  <div class="abs" style="left:255px;top:120px">
    <div style="font-size:11px;font-weight:800">Section Slide</div>
    <div style="font-size:5.5px;margin-top:2px">Sub Divider Presentation</div>
  </div>
  <div class="brand on-dark abs" style="left:12px;bottom:8px">Marrowind Labs</div>
</section>

<!-- Row 5 -->
<section class="slide is-blue" style="left:33px;top:1587px">
  <svg class="layer" viewBox="0 0 367 207" preserveAspectRatio="none">
    <path d="M0 0H150C182 40 172 120 138 160C110 195 60 200 0 188Z" fill="#fff"/>
    <path role="img" aria-label="Portrait of a consultant in a blazer" d="M245 35C270 15 318 22 332 58C346 95 330 140 296 155C260 170 220 150 210 118C200 86 220 55 245 35Z" fill="url(#ph)"/>
  </svg>
  <div class="abs" style="left:14px;top:14px;width:120px">
    <div class="title">John Doe</div>
    <div class="sub" style="font-weight:400;color:var(--ink)">Lorem ipsum dolor sit amet,<br>consectetur adipiscing elit</div>
    <p class="quote" style="color:var(--blue);margin-top:8px;font-size:5px">“ Lorem Ipsum is simply dummy text of the printing and industry. Lorem Ipsum has been the industry's standard dummy text ever since the 1500s, when an unknown printer took a galley of type and scrembled it to make a type specimen book ”</p>
    <p class="body" style="margin-top:2px;color:var(--grey)">- John Doe</p>
  </div>
  <div class="foot"><span class="brand">Marrowind Labs</span><span class="url">www.marrowindlabs.se <i></i></span></div>
</section>

<section class="slide is-blue" style="left:417px;top:1587px">
  <div class="abs centered" style="left:0;right:0;top:52px">
    <div style="margin:0 auto;width:16px;height:16px;border-radius:50%;background:var(--navy);font-size:9px;font-weight:800;line-height:18px">“</div>
    <div style="width:240px;height:1px;background:#7da0da;margin:-8px auto 12px"></div>
    <p class="quote" style="font-size:8px;width:260px;margin:0 auto">Lorem ipsum dolor sit amet, te ullum corpora delicata duo. Rebum insolens pri eu. No alia tota modus qui.</p>
    <p style="font-size:5.5px;margin-top:6px">- John Doe</p>
  </div>
  <div class="foot"><span class="brand">Marrowind Labs</span><span class="url">www.marrowindlabs.se <i></i></span></div>
</section>

<section class="slide" style="left:800px;top:1587px">
  <div class="title abs" style="left:14px;top:12px">Content With Icons</div>
  <div class="abs" style="left:14px;top:28px;width:339px;height:1px;background:#c9d3e6"></div>
  <div class="ic-row" style="left:40px;top:40px;text-align:right"><div><strong>Heading 1</strong><span>Lorem ipsum dolor sit amet,<br>consectetur adipiscing elit</span></div><svg width="18" height="16" viewBox="0 0 18 16"><path d="M3 2C8-1 16 1 17 7C18 13 11 16 6 14C1 12-1 5 3 2Z" fill="var(--navy)"/><path d="M6 10l3-3 2 2 3-4" stroke="#fff" fill="none"/></svg></div>
  <div class="ic-row" style="left:40px;top:80px;text-align:right"><div><strong>Heading 2</strong><span>Lorem ipsum dolor sit amet,<br>consectetur adipiscing elit</span></div><svg width="18" height="16" viewBox="0 0 18 16"><path d="M3 2C8-1 16 1 17 7C18 13 11 16 6 14C1 12-1 5 3 2Z" fill="var(--navy)"/><circle cx="9" cy="8" r="3" stroke="#fff" fill="none"/></svg></div>
  <div class="ic-row" style="left:40px;top:120px;text-align:right"><div><strong>Heading 3</strong><span>Lorem ipsum dolor sit amet,<br>consectetur adipiscing elit</span></div><svg width="18" height="16" viewBox="0 0 18 16"><path d="M3 2C8-1 16 1 17 7C18 13 11 16 6 14C1 12-1 5 3 2Z" fill="var(--navy)"/><path d="M5 8h8M9 4v8" stroke="#fff"/></svg></div>
  <div class="ic-row" style="left:200px;top:40px"><svg width="18" height="16" viewBox="0 0 18 16"><path d="M3 2C8-1 16 1 17 7C18 13 11 16 6 14C1 12-1 5 3 2Z" fill="var(--navy)"/><rect x="6" y="5" width="6" height="6" stroke="#fff" fill="none"/></svg><div><strong>Heading 4</strong><span>Lorem ipsum dolor sit amet,<br>consectetur adipiscing elit</span></div></div>
  <div class="ic-row" style="left:200px;top:80px"><svg width="18" height="16" viewBox="0 0 18 16"><path d="M3 2C8-1 16 1 17 7C18 13 11 16 6 14C1 12-1 5 3 2Z" fill="var(--navy)"/><path d="M5 11l4-6 4 6z" stroke="#fff" fill="none"/></svg><div><strong>Heading 5</strong><span>Lorem ipsum dolor sit amet,<br>consectetur adipiscing elit</span></div></div>
  <div class="ic-row" style="left:200px;top:120px"><svg width="18" height="16" viewBox="0 0 18 16"><path d="M3 2C8-1 16 1 17 7C18 13 11 16 6 14C1 12-1 5 3 2Z" fill="var(--navy)"/><path d="M5 8l3 3 5-6" stroke="#fff" fill="none"/></svg><div><strong>Heading 6</strong><span>Lorem ipsum dolor sit amet,<br>consectetur adipiscing elit</span></div></div>
  <div class="foot"><span class="brand">Marrowind Labs</span><span class="url">www.marrowindlabs.se <i></i></span></div>
</section>

<!-- Row 6 -->
<section class="slide" style="left:33px;top:1812px">
  <div class="title abs" style="left:14px;top:12px">The “3 Circles” Slide</div>
  <svg class="layer" viewBox="0 0 367 207" preserveAspectRatio="none">
    <circle cx="128" cy="85" r="36" fill="var(--navy)"/>
    <circle cx="240" cy="85" r="36" fill="var(--navy)"/>
    <circle cx="184" cy="85" r="36" fill="var(--sky)" opacity=".9"/>
    <g fill="#fff" font-size="5" font-weight="800" font-family="Nunito Sans, sans-serif" text-anchor="middle">
      <text x="120" y="100">CULTURE</text><text x="184" y="98">BUSINESS</text><text x="184" y="105">INTENT</text><text x="248" y="100">TECHNOLOGY</text>
    </g>
    <path d="M118 78h8M122 74v8" stroke="#fff" stroke-width="1.5"/>
    <path d="M178 74l6 -4 6 4v8h-12z" stroke="#fff" fill="none"/>
    <path d="M242 82v-4M246 82v-7M250 82v-10" stroke="#fff" stroke-width="1.5"/>
  </svg>
  <p class="body abs centered" style="left:88px;top:130px;width:70px">Lorem ipsum dolor sit amet, te ulum corpora delicata duo. Rebum insolens pri eu.</p>
  <p class="body abs centered" style="left:150px;top:130px;width:70px">Lorem ipsum dolor sit amet, te ulum corpora delicata duo. Rebum insolens pri eu.</p>
  <p class="body abs centered" style="left:212px;top:130px;width:70px">Lorem ipsum dolor sit amet, te ulum corpora delicata duo. Rebum insolens pri eu.</p>
  <div class="foot"><span class="brand">Marrowind Labs</span><span class="url">www.marrowindlabs.se <i></i></span></div>
</section>

<section class="slide" style="left:417px;top:1812px">
  <div class="title abs" style="left:14px;top:12px">Our Consultants</div>
  <div class="abs" style="left:14px;top:28px;width:339px;height:1px;background:#c9d3e6"></div>
  <div class="person abs centered" style="left:20px;top:40px;width:70px"><div class="photo" style="width:40px;height:48px;margin:0 auto;border-radius:45% 55% 40% 60%" role="img" aria-label="Portrait of consultant"></div><strong>Noel Harwick</strong><span>Lorem ipsum dolor sit amet,<br>consectetur adipiscing elit</span></div>
  <div class="person abs centered" style="left:105px;top:40px;width:70px"><div class="photo" style="width:40px;height:48px;margin:0 auto;border-radius:55% 45% 60% 40%" role="img" aria-label="Portrait of consultant"></div><strong>Ingrid Falk</strong><span>Lorem ipsum dolor sit amet,<br>consectetur adipiscing elit</span></div>
  <div class="person abs centered" style="left:190px;top:40px;width:70px"><div class="photo" style="width:40px;height:48px;margin:0 auto;border-radius:45% 55% 40% 60%" role="img" aria-label="Portrait of consultant"></div><strong>Tomas Brevik</strong><span>Lorem ipsum dolor sit amet,<br>consectetur adipiscing elit</span></div>
  <div class="person abs centered" style="left:275px;top:40px;width:70px"><div class="photo" style="width:40px;height:48px;margin:0 auto;border-radius:55% 45% 60% 40%" role="img" aria-label="Portrait of consultant"></div><strong>Lena Ostberg</strong><span>Lorem ipsum dolor sit amet,<br>consectetur adipiscing elit</span></div>
  <div class="foot"><span class="brand">Marrowind Labs</span><span class="url">www.marrowindlabs.se <i></i></span></div>
</section>

<section class="slide" style="left:800px;top:1812px">
  <div class="title abs" style="left:14px;top:12px">Graph Slides Sample</div>
  <svg class="layer" viewBox="0 0 367 207" preserveAspectRatio="none">
    <circle cx="183" cy="105" r="42" fill="none" stroke="var(--blue)" stroke-width="20" stroke-dasharray="29 4"/>
    <circle cx="183" cy="105" r="25" fill="#fff"/>
    <text x="183" y="104" font-size="5.5" font-weight="800" fill="var(--navy)" text-anchor="middle" font-family="Nunito Sans, sans-serif">MARROWIND</text>
    <text x="183" y="111" font-size="5.5" font-weight="800" fill="var(--navy)" text-anchor="middle" font-family="Nunito Sans, sans-serif">LABS</text>
  </svg>
  <p class="body abs" style="left:40px;top:50px;width:80px;text-align:right">Lorem ipsum dolor sit amet, consectetur adipiscing elit</p>
  <p class="body abs" style="left:30px;top:98px;width:80px;text-align:right">Lorem ipsum dolor sit amet, consectetur adipiscing elit</p>
  <p class="body abs" style="left:40px;top:146px;width:80px;text-align:right">Lorem ipsum dolor sit amet, consectetur adipiscing elit</p>
  <p class="body abs" style="left:247px;top:50px;width:80px">Lorem ipsum dolor sit amet, consectetur adipiscing elit</p>
  <p class="body abs" style="left:257px;top:98px;width:80px">Lorem ipsum dolor sit amet, consectetur adipiscing elit</p>
  <p class="body abs" style="left:247px;top:146px;width:80px">Lorem ipsum dolor sit amet, consectetur adipiscing elit</p>
  <div class="foot"><span class="brand">Marrowind Labs</span><span class="url">www.marrowindlabs.se <i></i></span></div>
</section>

<!-- Row 7 -->
<section class="slide" style="left:33px;top:2037px">
  <div class="title abs" style="left:14px;top:12px">Data Sample</div>
  <svg class="layer" viewBox="0 0 367 207" preserveAspectRatio="none">
    <g fill="none" stroke-width="6">
      <circle cx="72" cy="72" r="22" stroke="#dfe6f2"/><circle cx="72" cy="72" r="22" stroke="var(--navy)" stroke-dasharray="34.6 200" transform="rotate(-90 72 72)"/>
      <circle cx="183" cy="72" r="22" stroke="#dfe6f2"/><circle cx="183" cy="72" r="22" stroke="var(--blue)" stroke-dasharray="65 200" transform="rotate(-90 183 72)"/>
      <circle cx="294" cy="72" r="22" stroke="#dfe6f2"/><circle cx="294" cy="72" r="22" stroke="var(--sky)" stroke-dasharray="96.8 200" transform="rotate(-90 294 72)"/>
    </g>
    <g font-size="8" font-weight="800" fill="var(--navy)" text-anchor="middle" font-family="Nunito Sans, sans-serif"><text x="72" y="75">25%</text><text x="183" y="75">47%</text><text x="294" y="75">70%</text></g>
  </svg>
  <div class="abs centered" style="left:32px;top:108px;width:80px"><div class="sub">LOREM IPSUM</div><p class="body">Lorem ipsum dolor sit amet, te ulum corpora delicata duo. Rebum insolens pri eu. No alia tota modus qui</p></div>
  <div class="abs centered" style="left:143px;top:108px;width:80px"><div class="sub">LOREM IPSUM</div><p class="body">Lorem ipsum dolor sit amet, te ulum corpora delicata duo. Rebum insolens pri eu. No alia tota modus qui</p></div>
  <div class="abs centered" style="left:254px;top:108px;width:80px"><div class="sub">LOREM IPSUM</div><p class="body">Lorem ipsum dolor sit amet, te ulum corpora delicata duo. Rebum insolens pri eu. No alia tota modus qui</p></div>
  <div class="foot"><span class="brand">Marrowind Labs</span><span class="url">www.marrowindlabs.se <i></i></span></div>
</section>

<section class="slide" style="left:417px;top:2037px">
  <div class="title abs" style="left:14px;top:12px">Timeline Sample</div>
  <svg class="layer" viewBox="0 0 367 207" preserveAspectRatio="none">
    <g font-size="5.5" font-weight="800" fill="#fff" font-family="Nunito Sans, sans-serif" text-anchor="middle">
      <path d="M55 105h38l5 6-5 6h-38z" fill="var(--navy)"/><text x="75" y="113">2010</text>
      <path d="M98 105h38l5 6-5 6h-38l5-6z" fill="var(--blue)"/><text x="120" y="113">2011</text>
      <path d="M141 105h38l5 6-5 6h-38l5-6z" fill="var(--navy)"/><text x="163" y="113">2012</text>
      <path d="M184 105h38l5 6-5 6h-38l5-6z" fill="var(--blue)"/><text x="206" y="113">2013</text>
      <path d="M227 105h38l5 6-5 6h-38l5-6z" fill="var(--navy)"/><text x="249" y="113">2014</text>
      <path d="M270 105h38l5 6-5 6h-38l5-6z" fill="var(--blue)"/><text x="292" y="113">2015</text>
    </g>
    <g stroke="#9fb2d6" stroke-width=".6"><line x1="75" y1="80" x2="75" y2="105"/><line x1="163" y1="55" x2="163" y2="105"/><line x1="249" y1="60" x2="249" y2="105"/><line x1="120" y1="117" x2="120" y2="150"/><line x1="206" y1="117" x2="206" y2="150"/><line x1="292" y1="117" x2="292" y2="150"/></g>
    <g fill="var(--navy)"><circle cx="75" cy="96" r="4"/><circle cx="120" cy="96" r="4"/><circle cx="163" cy="96" r="4"/><circle cx="206" cy="96" r="4"/><circle cx="249" cy="96" r="4"/><circle cx="292" cy="96" r="4"/></g>
  </svg>
  <p class="body abs" style="left:80px;top:66px;width:60px">Lorem ipsum dolor sit amet, consectetur adipiscing elit</p>
  <p class="body abs" style="left:168px;top:42px;width:60px">Lorem ipsum dolor sit amet, consectetur adipiscing elit</p>
  <p class="body abs" style="left:254px;top:46px;width:60px">Lorem ipsum dolor sit amet, consectetur adipiscing elit</p>
  <p class="body abs" style="left:125px;top:140px;width:60px">Lorem ipsum dolor sit amet, consectetur adipiscing elit</p>
  <p class="body abs" style="left:211px;top:140px;width:60px">Lorem ipsum dolor sit amet, consectetur adipiscing elit</p>
  <p class="body abs" style="left:297px;top:140px;width:56px">Lorem ipsum dolor sit amet, consectetur adipiscing elit</p>
  <div class="foot"><span class="brand">Marrowind Labs</span><span class="url">www.marrowindlabs.se <i></i></span></div>
</section>

<section class="slide" style="left:800px;top:2037px">
  <svg class="layer" viewBox="0 0 367 207" preserveAspectRatio="none">
    <path d="M0 0H367V72C310 90 260 60 183 88C110 114 60 80 0 95Z" fill="var(--navy)"/>
    <path d="M0 85C60 72 110 104 183 80C260 55 310 82 367 66V72C310 90 260 60 183 88C110 114 60 80 0 95Z" fill="var(--blue)"/>
    <circle cx="70" cy="92" r="9" fill="var(--navy)" stroke="#fff" stroke-width="1.5"/>
    <circle cx="183" cy="87" r="9" fill="var(--blue)" stroke="#fff" stroke-width="1.5"/>
    <circle cx="296" cy="72" r="9" fill="var(--green)" stroke="#fff" stroke-width="1.5"/>
    <path d="M66 95l3-4 3 2 3-4M179 84h8v6h-8zM292 72l3 3 5-5" stroke="#fff" fill="none"/>
  </svg>
  <div class="abs centered" style="left:0;right:0;top:12px;color:#fff">
    <div class="title">Content With Icons</div>
    <p style="font-size:5px;margin-top:4px">Lorem ipsum dolor sit amet, te ulum corpora delicata duo.<br>Rebum insolens pri eu. No alia tota modus qui.</p>
  </div>
  <div class="abs centered" style="left:30px;top:106px;width:80px"><div class="sub">HEADING 1</div><p class="body">Lorem ipsum dolor sit amet,<br>consectetur adipiscing elit</p></div>
  <div class="abs centered" style="left:143px;top:101px;width:80px"><div class="sub">HEADING 2</div><p class="body">Lorem ipsum dolor sit amet,<br>consectetur adipiscing elit</p></div>
  <div class="abs centered" style="left:256px;top:86px;width:80px"><div class="sub" style="color:var(--green)">HEADING 3</div><p class="body">Lorem ipsum dolor sit amet,<br>consectetur adipiscing elit</p></div>
  <div class="foot"><span class="brand">Marrowind Labs</span><span class="url">www.marrowindlabs.se <i></i></span></div>
</section>

<!-- Row 8 -->
<section class="slide" style="left:33px;top:2262px">
  <div class="title abs" style="left:14px;top:12px">Chart Sample</div>
  <div class="abs centered" style="left:0;right:0;top:30px;font-size:6px;color:var(--ink)">LOREM IPSUM DOLOR SIT AMET</div>
  <svg class="layer" viewBox="0 0 367 207" preserveAspectRatio="none">
    <g stroke="#e1e6ef" stroke-width=".5"><line x1="40" y1="60" x2="340" y2="60"/><line x1="40" y1="85" x2="340" y2="85"/><line x1="40" y1="110" x2="340" y2="110"/><line x1="40" y1="135" x2="340" y2="135"/><line x1="40" y1="160" x2="340" y2="160"/></g>
    <rect x="50" y="80" width="11" height="80" fill="var(--navy)"/>
    <rect x="80" y="120" width="11" height="40" fill="var(--navy)"/>
    <rect x="110" y="95" width="11" height="65" fill="var(--green)"/>
    <rect x="140" y="75" width="11" height="85" fill="var(--navy)"/>
    <rect x="170" y="118" width="11" height="42" fill="var(--navy)"/>
    <rect x="200" y="138" width="11" height="22" fill="var(--green)"/>
    <rect x="230" y="66" width="11" height="94" fill="var(--navy)"/>
    <rect x="260" y="112" width="11" height="48" fill="var(--navy)"/>
    <rect x="290" y="128" width="11" height="32" fill="var(--green)"/>
    <rect x="320" y="82" width="11" height="78" fill="var(--navy)"/>
    <g font-size="3.8" fill="var(--grey)" font-family="Nunito Sans, sans-serif"><text x="46" y="167">Category 1</text><text x="76" y="167">Category 2</text><text x="106" y="167">Category 3</text><text x="136" y="167">Category 4</text><text x="166" y="167">Category 5</text><text x="196" y="167">Category 6</text><text x="226" y="167">Category 7</text><text x="256" y="167">Category 8</text><text x="286" y="167">Category 9</text><text x="315" y="167">Category 10</text></g>
  </svg>
  <div class="foot"><span class="brand">Marrowind Labs</span><span class="url">www.marrowindlabs.se <i></i></span></div>
</section>

<section class="slide" style="left:417px;top:2262px">
  <div class="title abs" style="left:14px;top:12px">Content With Image</div>
  <div class="abs photo" style="left:0;top:30px;width:122px;height:60px" role="img" aria-label="Photo of a team in discussion"></div>
  <div class="tile" style="left:122px;top:30px;width:122px;height:60px;background:var(--navy)"><strong>Heading 2</strong><span>Lorem ipsum dolor sit amet,<br>consectetur adipiscing elit</span></div>
  <div class="abs photo" style="left:244px;top:30px;width:123px;height:60px" role="img" aria-label="Photo of colleagues at a meeting"></div>
  <div class="tile" style="left:0;top:90px;width:122px;height:60px;background:var(--navy);padding-top:26px"><strong>Heading 1</strong><span>Lorem ipsum dolor sit amet,<br>consectetur adipiscing elit</span></div>
  <div class="abs photo" style="left:122px;top:90px;width:122px;height:60px" role="img" aria-label="Photo of a workshop session"></div>
  <div class="tile" style="left:244px;top:90px;width:123px;height:60px;background:var(--blue);padding-top:26px"><strong>Heading 3</strong><span>Lorem ipsum dolor sit amet,<br>consectetur adipiscing elit</span></div>
  <div class="foot"><span class="brand">Marrowind Labs</span><span class="url">www.marrowindlabs.se <i></i></span></div>
</section>

<section class="slide is-blue" style="left:800px;top:2262px">
  <svg class="layer" viewBox="0 0 367 207" preserveAspectRatio="none">
    <path d="M367 0H190C165 45 170 130 200 170C220 195 260 207 290 207H367Z" fill="var(--navy)"/>
    <path role="img" aria-label="Photo of a workplace scene" d="M367 0H210C188 45 192 125 220 162C238 188 272 200 300 200H367Z" fill="url(#ph)"/>
  </svg>
  <div class="abs" style="left:30px;top:75px">
    <div class="big-brand">Marrowind Labs</div>
    <div style="font-size:14px;font-weight:800;margin-top:12px">THANK YOU</div>
  </div>
  <div class="abs" style="left:30px;bottom:12px;font-size:5px">www.marrowindlabs.se</div>
</section>

</body>
</html>
```